Brightfield Training Course Outline re-design

We are wanting to re-design our template for course outlines. Course outlines are provided to prospective students wanting to find out more information about a course. Our website was recently revamped so we would want the new course outlines to have a similar look and feel to our website: www.brightfieldtraining.com.au
I have attached a current course outline. All content from the current outline must come across to the new one. We want to appeal to adult students wanting to work with children. We emphasise flexible timeframes, easy-to-use online system, prompt and friendly support from a trainer. We want to inspire people to engage in education and change their lives. This is reflected in our motto - Study | Brightfield | Achieve.
Ideally, this will become a template for other course outlines, so if the file can be provided in PDF as well as an editable format it would be greatly appreciated.
The colour codes from our website are:
Aqua: #81c9bd
Grey: #939598
Blue: #000080
Looking forward to responses.
Happy to email any images or logos needed.

Target Market(s)

Mums with children wanting to re-enter the workforce

Requirements
Must have
• All content from current course outline must come across.
• Brightfield Training logo

```html
<!DOCTYPE html>
<html lang="en">
<head>
<meta charset="utf-8">
<title>Brightfield Training – Course Outline CHC30213</title>
<link rel="stylesheet" href="https://fonts.googleapis.com/css2?family=Montserrat:wght@700;800&family=Open+Sans:wght@400;600;700&display=swap">
<style>
:root{
  --navy:#2d2a82;
  --navy-deep:#221f6b;
  --aqua:#81c9bd;
  --grey:#939598;
  --paper:#ffffff;
  --table:#cfcfe6;
  --bg:#e3e3e5;
  --ink:#3a3a4a;
}
*{box-sizing:border-box;margin:0;padding:0}
html,body{width:1200px;height:792px;overflow:hidden;background:var(--bg)}
body{position:relative;font-family:"Open Sans",Arial,sans-serif;color:var(--ink)}
.spread{position:absolute;top:194px;width:570px;height:404px;display:flex;box-shadow:0 6px 18px rgba(0,0,0,.18)}
.spread--outer{left:22px}
.spread--inner{left:608px}
.page{position:relative;width:285px;height:404px;background:var(--paper);overflow:hidden}
.page + .page{border-left:1px solid #e6e6ec}
.abs{position:absolute}
h2{font-family:"Montserrat",Arial,sans-serif;font-weight:800;text-transform:uppercase;font-size:8px;line-height:1.05;color:var(--navy);margin:0 0 2px}
.panel h2,.on-navy h2{color:#fff}
p,li{font-size:4.6px;line-height:1.35}
p + p{margin-top:2px}
p + h2,ul + h2,ol + h2{margin-top:4px}
.panel{background:var(--navy);color:#fff;border-radius:6px;padding:7px 8px}
.panel p,.panel li{color:#fff}
ul.units{list-style:none}
ul.units li{padding-left:5px;position:relative}
ul.units li::before{content:"";position:absolute;left:0;top:2px;width:2.2px;height:2.2px;border-radius:50%;background:currentColor}
ul.units b{font-weight:700}
ol.steps{padding-left:7px}
.photo{border-radius:7px}
.brand{display:flex;align-items:center;gap:4px;font-family:"Montserrat",Arial,sans-serif;font-weight:800;color:var(--navy);font-size:11px}
.brand-mark{width:9px;height:9px;background:var(--navy)}
.title-box{right:0;top:10px;width:150px;height:54px;background:var(--navy);border-radius:8px 0 0 8px;border-left:4px solid var(--aqua);padding:7px 9px;color:#fff}
.title-box .kicker{font-family:"Montserrat",Arial,sans-serif;font-weight:800;font-size:13px;letter-spacing:.2px}
.title-box .course{font-family:"Montserrat",Arial,sans-serif;font-weight:700;font-size:7.2px;line-height:1.2;margin-top:2px}
.contact .rto{font-family:"Montserrat",Arial,sans-serif;font-weight:800;font-size:6px;color:var(--navy);margin:5px 0 2px}
.contact .phone{font-family:"Montserrat",Arial,sans-serif;font-weight:800;font-size:8px;color:var(--navy)}
.web-bar{left:0;bottom:8px;width:128px;height:14px;background:var(--aqua);color:var(--navy);font-family:"Montserrat",Arial,sans-serif;font-weight:800;font-size:5.6px;display:flex;align-items:center;padding-left:10px;border-radius:0 7px 7px 0}
.pay-band{height:9px;background:var(--aqua);border-radius:6px 6px 0 0;margin:-7px -8px 5px}
table.fees{width:100%;border-collapse:collapse;margin-top:4px;font-size:4.6px}
table.fees th{background:var(--aqua);color:var(--navy);font-weight:700;text-align:right;padding:1.5px 3px}
table.fees th:first-child{text-align:left}
table.fees td{background:var(--table);color:var(--navy);padding:1.5px 3px;border-top:1px solid #fff}
table.fees td:last-child{text-align:right;width:48px}
</style>
</head>
<body>

<section class="spread spread--outer">

  <article class="page page--back">
    <div class="abs photo" style="left:0;top:0;width:285px;height:196px;border-radius:0;background:linear-gradient(135deg,#bfc3cf,#8e93a6 55%,#c9ccd6)" role="img" aria-label="Photo of hands typing on a laptop keyboard"></div>
    <div class="abs on-navy" style="left:0;top:0;width:190px;height:92px;background:rgba(45,42,130,.9);border-radius:0 0 8px 0;padding:9px 10px;color:#fff">
      <h2>Student Support</h2>
      <p>Regardless of the study mode you select, you will have unlimited access to your trainer through phone, email and instant messaging. You may send your trainer drafts for feedback and contact them when needed. Your trainer has significant industry experience and will prove a valuable support throughout the course.</p>
      <h2>How to Enrol</h2>
      <p>Read the Student Handbook and this Course Outline. You have 3 different ways to enrol:</p>
      <ol class="steps">
        <li>Go to brightfieldtraining.com.au/enrol now to complete your enrolment online OR</li>
        <li>Download an Enrolment Form from our website and return by email or post OR</li>
        <li>Call us on 1300 555 018 to enrol over the phone</li>
      </ol>
    </div>
    <div class="abs panel" style="right:8px;top:150px;width:104px;height:112px">
      <h2 style="text-align:right">Course<br>Completion</h2>
      <p>On successful completion of all course requirements you will be issued a Nationally Recognised Certificate III in Education Support. All students completing the course will be required to complete a short student survey.</p>
    </div>
    <div class="abs" style="left:10px;top:204px;width:160px">
      <h2>Course Commencement</h2>
      <p>Upon receipt of your enrolment form a Brightfield Training staff member will contact you to conduct a pre-enrolment interview and to confirm your enrolment.</p>
      <h2>Course Induction</h2>
      <p>All Brightfield Training students will receive a course induction. Inductions may be completed face-to-face, via video call, or over the phone. During your induction your trainer will take time to explain how to navigate your course resources and assessments and provide you with some guidance on the depth and content expected in some of the different assessments.</p>
      <h2>First Aid</h2>
      <p>You have the option of selecting HLTAID003 Provide first aid as an elective unit within this course. Brightfield Training delivers this unit at select venues and dates. Alternatively, you may complete the first aid course with any provider in Australia. If this unit is not included in your course fee, you will need to pay the listed course fee to your first aid provider. Ensure that you are booking into a first aid course that includes the nationally recognised unit HLTAID003 Provide First Aid.</p>
    </div>
    <div class="abs" style="left:180px;top:272px;width:96px">
      <div class="brand" style="font-size:8.5px"><span class="brand-mark"></span>Brightfield Training</div>
    </div>
  </article>

  <article class="page page--front">
    <div class="abs brand" style="left:12px;top:32px"><span class="brand-mark"></span>Brightfield Training</div>
    <header class="abs title-box">
      <div class="kicker">COURSE OUTLINE</div>
      <div class="course">CHC30213 Certificate III<br>in Education Support</div>
    </header>
    <p class="abs" style="left:12px;top:70px;width:262px">Welcome to Brightfield Training (RTO# 40718). Thank you for considering us in the very important task of gaining a nationally recognised qualification. Please read this course outline and the student handbook prior to enrolling; these documents contain information crucial for successful study in this course.</p>
    <div class="abs photo" style="left:140px;top:96px;width:136px;height:76px;background:linear-gradient(135deg,#5c5a8c,#b7a79a 50%,#6f7c9a)" role="img" aria-label="Photo of a teacher helping two smiling students"></div>
    <div class="abs panel" style="left:8px;top:100px;width:126px;height:220px">
      <h2>About Certificate III in Education Support</h2>
      <p>This course is suitable if you are currently working or wanting to work as a teacher aide in a primary or secondary school. Recognised course consists of 17 units:</p>
      <ul class="units" style="margin-top:2px">
        <li><b>CHCECE006</b> Support behaviour of children and young people</li>
        <li><b>CHCEDS001</b> Comply with legislative, policy and industrial requirements</li>
        <li><b>CHCEDS007</b> Work effectively with students and colleagues</li>
        <li><b>CHCEDS016</b> Support learning for students with disabilities</li>
        <li><b>CHCEDS018</b> Support students with additional needs in the classroom</li>
        <li><b>CHCEDS002</b> Assist implementation of planned educational programs</li>
        <li><b>CHCEDS003</b> Contribute to student education in all developmental domains</li>
        <li><b>CHCDIV001</b> Work with diverse people</li>
        <li><b>CHCEDS008</b> Comply with school administrative requirements</li>
        <li><b>CHCEDS004</b> Contribute to organisation and management of classroom</li>
        <li><b>CHCEDS005</b> Support the development of literacy and oral language skills</li>
        <li><b>CHCEDS006</b> Support the development of numeracy skills</li>
        <li><b>CHCEDS017</b> Contribute to the health and safety of students</li>
        <li><b>HLTWHS001</b> Participate in work health and safety</li>
        <li><b>CHCDIV002</b> Promote Aboriginal and/or Torres Strait Islander cultural safety</li>
      </ul>
    </div>
    <div class="abs" style="left:142px;top:180px;width:134px">
      <h2>Elective Units <span style="font-size:4.4px;font-weight:700">(choose 3 from the following)</span></h2>
      <ul class="units">
        <li><b>CHCEDS024</b> Use educational strategies to support Aboriginal and/or Torres Strait Islander education</li>
        <li><b>CHCEDS012</b> Support learning and implementation of responsible behaviour</li>
        <li><b>CHCEDS022</b> Set up and sustain individual and small group learning areas</li>
        <li><b>CHCEDS011</b> Search and assess online information</li>
        <li><b>CHCEDS004</b> Communicate using augmentative and alternative strategies</li>
        <li><b>HLTAID003</b> Provide first aid*</li>
      </ul>
      <p>* Please read the first aid section in this document for further details on fees and conditions associated with selecting this unit.</p>
      <h2>Entry Requirements</h2>
      <p>It is expected that students have well developed written and verbal communication skills, basic numeracy skills and basic computer operating skills. A Working with Children Check (also known as a blue card in QLD) must be obtained prior to conducting your vocational placement. Refer to our website for links to each State or Territory agency responsible for administering working with children checks.</p>
    </div>
    <div class="abs contact" style="left:12px;top:324px;width:124px">
      <div class="rto">BRIGHTFIELD TRAINING RTO # 40718</div>
      <p>PO Box 2210 Carindale QLD 4152</p>
      <div class="phone">1300 555 018</div>
      <p>info@brightfieldtraining.com.au</p>
    </div>
    <div class="abs web-bar">www.brightfieldtraining.com.au</div>
  </article>

</section>

<section class="spread spread--inner">

  <article class="page page--inner-left">
    <div class="abs panel" style="left:8px;top:10px;width:269px;height:214px">
      <h2>Duration</h2>
      <p>You will have up to 2 years to complete but can progress at any pace. As a guide someone spending 8 hrs per week on assessment could expect to complete the course in approximately 7 – 9 months. Please note that students receiving government funding/subsidies may be obligated to complete in a set time frame.</p>
      <p>* Service Assist (education supplement): full time 40 weeks, part time 69 weeks</p>
      <h2>Study Mode</h2>
      <p>Delivery and assessment of this course can be customised. Please discuss your options with Brightfield Training to ensure that we have created the course that best suits you.</p>
      <h2>Self-Paced</h2>
      <p>Self-paced study means that you can study at times and locations that suit you. No assessment due dates and no timetabled lectures or webinars. You can choose to study online using an interactive online portal or via correspondence with all materials posted out to you. Fast track your study or take your time – the choice is yours.</p>
      <h2>Blended</h2>
      <p>Blended study has all the perks of self-paced study with the addition of face-to-face sessions with your trainer. You can book as many or as few face-to-face sessions as you like – the price in the table below is for the self-paced option.</p>
      <h2>Online or Correspondence?</h2>
      <p>The course consists of two key components: Theory and Practical. For the theory component you may opt to receive course resources via correspondence or online. The online course is interactive, meaning less reading and more visually engaging resources. Correspondence resources are in a hardcopy format. Resources are presented in a student portfolio for easy management. Assessment is provided on a USB stick.</p>
    </div>
    <div class="abs" style="left:10px;top:232px;width:124px">
      <h2>Practical</h2>
      <p>Students not currently working in the education support industry will be required to complete 100 hours of practical placement as part of their study. You may choose to do your placement as a full time block or part time (e.g. 2 days per week). The placement can be completed at any stage during your course. Brightfield Training can arrange your placement for you or you can arrange your own. Additional hours may be required for students on a traineeship. School leavers or those that have limited experience will be encouraged to develop skills in a work setting. In some instances the number of placement hours will need to be negotiated between the student, the trainer and the placement.</p>
    </div>
    <div class="abs" style="left:142px;top:230px;width:134px">
      <h2>Assessment</h2>
      <p>Your assessment consists of two key areas:</p>
      <p><b>Theory Assessment</b> that may include text activities, written questions, case studies, projects, evidence portfolios.</p>
      <p><b>Practical Assessment</b> that includes demonstration of your skills in the workplace. Recorded as observations by your supervisor, practical placement person or trainer.</p>
    </div>
    <div class="abs photo" style="left:142px;top:300px;width:136px;height:96px;background:linear-gradient(135deg,#3b3f6e,#8b91b0 50%,#c5b8a8)" role="img" aria-label="Photo of a person studying on a laptop showing an online learning screen"></div>
  </article>

  <article class="page page--inner-right">
    <div class="abs" style="left:10px;top:12px;width:142px">
      <h2>Government Funding</h2>
      <p>This course is approved for funding through the following programs:</p>
      <ul class="units">
        <li>Certificate 3 Guarantee (eligible QLD residents only)</li>
        <li>Queensland Traineeships (for new employees)</li>
        <li>Service Assist Education Supplement</li>
      </ul>
      <p>Funding is subject to our eligibility checklist and we will let you know if you or your employer may attract a subsidy.</p>
      <h2>Certificate 3 Guarantee</h2>
      <p>The Certificate 3 Guarantee aims to assist people gain their first post-school Certificate III qualification regardless of their current employment status. To be eligible you must:</p>
      <ul class="units">
        <li>be 15 years or above and no longer be at school</li>
        <li>permanently reside in Queensland</li>
        <li>be an Australian citizen or New Zealand citizen or permanent resident (including humanitarian visa holders) or temporary resident on the pathway to permanent residency</li>
        <li>not hold or be currently enrolled in a post school certificate III or higher level qualification</li>
      </ul>
      <p>Students approved for the Certificate 3 Guarantee must pay a student contribution fee. Concession students will pay a reduced contribution fee.</p>
    </div>
    <div class="abs photo" style="left:160px;top:10px;width:117px;height:92px;background:linear-gradient(135deg,#2f2c86,#5b5ea8 50%,#3a3890)" role="img" aria-label="Navy toned photo of a teacher aide with school students"></div>
    <div class="abs photo" style="left:160px;top:108px;width:117px;height:96px;background:linear-gradient(135deg,#3b9f86,#6cc3a6 50%,#2c8a78)" role="img" aria-label="Green toned photo of an educator smiling with young children"></div>
    <div class="abs panel" style="left:8px;top:226px;width:269px;height:168px">
      <div class="pay-band"></div>
      <h2>Payment</h2>
      <p>The course fees quoted below are inclusive of all mandatory course resources. Additional fees apply if you select the unit HLTAID003 Provide first aid as an elective unit. Please read the first aid section in this document for further details.</p>
      <table class="fees">
        <tr><th>CHC30213 Certificate III in Education Support</th><th>Self-Paced</th></tr>
        <tr><td>Full fee (including those receiving the education supplement through Service Assist), OR</td><td>$1,980</td></tr>
        <tr><td>Students who qualify for the Certificate 3 Guarantee:</td><td></td></tr>
        <tr><td>Standard student contribution fee</td><td>$500</td></tr>
        <tr><td>Concession student contribution fee – concessional students</td><td>$400</td></tr>
        <tr><td>Student contribution fee – Yr 12 fee free students</td><td>$0</td></tr>
      </table>
      <p style="margin-top:4px">Please add $600 to above prices if you would like the blended mode of training (includes 4 onsite sessions and is only available to those in SE QLD region).</p>
      <p>Payment plans are offered at no additional cost! All fees quoted above can be incorporated into a payment plan. You nominate the payment periods (i.e. weekly, fortnightly or monthly). You nominate the amount you are comfortable paying each period (i.e. $50, $100, $200, etc.).</p>
    </div>
  </article>

</section>

</body>
</html>
```